Tariq Goldsmiths Stationary Contest

Pakistan’s largest Jewellery, Diamond and luxury watches store requires professional stationery. We have a long list of are trusted clients since 1959, our third generation has successfully maintained and sustained the legacy and excellence in the sector.

We require stationery template as part of this contest. The stationery can be double sided.

We prefer a design that makes use of some of the premium business stationery printing options, such as foil stamping, embossing/debossing, painted edges, spot UV etc (doesn't have to use all these options, only what you feel works, but we are looking for a design that stands out and is memorable and these nice touches have that effect.)

We want an eye catching, innovative, high end professional looking stationery for an out of box design that blends well with our new logo (attached). We want the design to be an out of box solution, you may use any element to compliment the logo. You may consider incorporating watermark etc, highlighting our products (Gold and Diamond Jewellery in addition to Luxury watches)

Company details are as follows;

Company name: Tariq Goldsmiths
Contact Person: Farhan Qureshi
Designation: Business Development Consultant
Mobile: +92 333 815 6042
Email: farhanqureshi@mailvale.com
Website: www.tariqgoldsmiths.com

Target Market(s)

Matrimonial, Elite & Businesses class, Upmarket

Font styles to use
Other font styles liked:
• Designers choice

Colors

Designer to choose colors to be used in the design.

Requirements
Must have
• Look and feel: Upmarket, innovative, Modern, Professional, graceful, Elegant, designer stuff.
Nice to have
• Unique design

```html
<!DOCTYPE html>
<html lang="en">
<head>
<meta charset="utf-8">
<title>Tariq Goldsmiths – Business Card</title>
<link href="https://fonts.googleapis.com/css2?family=Open+Sans:wght@400;600;700&display=swap" rel="stylesheet">
<style>
  :root{
    --stage:#d8ab3b;
    --gold-deep:#c08d14;
    --gold-mid:#d9a40c;
    --gold-bright:#f0c000;
    --paper:#ffffff;
    --ink:#3a3a3a;
    --accent:#c9980f;
  }
  *{margin:0;padding:0;box-sizing:border-box}
  html,body{width:1200px;height:914px;overflow:hidden}
  body{
    background:var(--stage);
    font-family:"Open Sans",Arial,sans-serif;
    display:flex;align-items:center;justify-content:center;gap:90px;
  }
  .card{
    position:relative;width:320px;height:560px;
    box-shadow:0 14px 30px rgba(90,60,0,.25);
    overflow:hidden;
  }
  .card-notch{
    position:absolute;left:50%;width:36px;height:12px;transform:translateX(-50%);
  }

  /* back: contact side */
  .card-back{background:var(--paper)}
  .card-back .card-notch{top:0;background:var(--gold-deep);clip-path:polygon(0 0,100% 0,78% 100%,22% 100%)}
  .back-brand{
    position:absolute;top:92px;left:0;right:0;
    display:flex;align-items:center;gap:14px;
  }
  .back-brand .rule{width:60px;height:3px;background:var(--accent)}
  .brand-dot{width:14px;height:14px;border-radius:50%;background:var(--accent);flex:none}
  .back-brand .brand-name{
    font-weight:700;font-size:17px;letter-spacing:1.5px;text-transform:uppercase;color:var(--ink);
  }
  .contact-list{
    position:absolute;top:200px;left:36px;right:24px;list-style:none;
    font-size:13px;line-height:1.35;color:var(--ink);
  }
  .contact-list li{display:flex;gap:10px;margin-bottom:12px;align-items:flex-start}
  .contact-list svg{flex:none;width:16px;height:16px;margin-top:1px}

  /* front: name side */
  .card-front{
    background:linear-gradient(100deg,var(--gold-deep) 0%,var(--gold-mid) 55%,var(--gold-bright) 100%);
    color:#fff;text-align:center;
  }
  .card-front .card-notch{bottom:0;background:#a97a0c;clip-path:polygon(22% 0,78% 0,100% 100%,0 100%)}
  .front-brand{
    position:absolute;top:160px;left:0;right:0;
    display:flex;flex-direction:column;align-items:center;gap:26px;
  }
  .front-brand .brand-dot{width:22px;height:22px;background:#fff}
  .front-brand .brand-line{display:flex;align-items:center;gap:14px;width:100%}
  .front-brand .rule{flex:1;height:3px;background:#fff}
  .front-brand .brand-name{
    font-weight:700;font-size:18px;letter-spacing:2px;text-transform:uppercase;white-space:nowrap;
  }
  .holder{position:absolute;top:345px;left:0;right:0}
  .holder-name{font-weight:700;font-size:22px}
  .holder-role{font-size:12.5px;margin-top:6px;letter-spacing:.3px}
</style>
</head>
<body>

  <section class="card card-back" aria-label="Card back with contact details">
    <span class="card-notch"></span>
    <div class="back-brand">
      <span class="rule"></span>
      <span class="brand-dot"></span>
      <span class="brand-name">Tariq Goldsmiths</span>
    </div>
    <ul class="contact-list">
      <li>
        <svg viewBox="0 0 16 16"><circle cx="8" cy="8" r="8" fill="#c9980f"/><path d="M8 3.5a3 3 0 0 0-3 3c0 2.2 3 5.5 3 5.5s3-3.3 3-5.5a3 3 0 0 0-3-3z" fill="#fff"/><circle cx="8" cy="6.5" r="1.1" fill="#c9980f"/></svg>
        <span>14 Garden Arcade, Canal Road,<br>Lahore, Pakistan</span>
      </li>
      <li>
        <svg viewBox="0 0 16 16"><circle cx="8" cy="8" r="8" fill="#c9980f"/><path d="M5.3 4h1.6l.7 2-1 .8a6 6 0 0 0 2.6 2.6l.8-1 2 .7v1.6c0 .5-.4.8-.9.8A7 7 0 0 1 4.5 4.9c0-.5.3-.9.8-.9z" fill="#fff"/></svg>
        <span>+92 333 815 6042</span>
      </li>
      <li>
        <svg viewBox="0 0 16 16"><circle cx="8" cy="8" r="8" fill="#c9980f"/><rect x="4.5" y="4" width="7" height="8" rx="1" fill="#fff"/><rect x="6" y="5.5" width="4" height="2" fill="#c9980f"/></svg>
        <span>042-35410287-89</span>
      </li>
      <li>
        <svg viewBox="0 0 16 16"><circle cx="8" cy="8" r="8" fill="#c9980f"/><rect x="4" y="5" width="8" height="6" rx=".6" fill="#fff"/><path d="M4 5.3l4 3 4-3" stroke="#c9980f" stroke-width=".9" fill="none"/></svg>
        <span>farhanqureshi@mailvale.com</span>
      </li>
      <li>
        <svg viewBox="0 0 16 16"><circle cx="8" cy="8" r="8" fill="#c9980f"/><circle cx="8" cy="8" r="4" fill="none" stroke="#fff" stroke-width="1"/><path d="M4 8h8M8 4c-2 2.4-2 5.6 0 8M8 4c2 2.4 2 5.6 0 8" stroke="#fff" stroke-width=".8" fill="none"/></svg>
        <span>www.tariqgoldsmiths.com</span>
      </li>
    </ul>
  </section>

  <section class="card card-front" aria-label="Card front with name and title">
    <div class="front-brand">
      <span class="brand-dot"></span>
      <div class="brand-line">
        <span class="rule"></span>
        <span class="brand-name">Tariq Goldsmiths</span>
        <span class="rule"></span>
      </div>
    </div>
    <div class="holder">
      <p class="holder-name">Farhan Qureshi</p>
      <p class="holder-role">Business Development Consultant</p>
    </div>
    <span class="card-notch"></span>
  </section>

</body>
</html>
```